Avocado Oil label - upmarket elegant design

We are a distributor of healthy and organic food in a process of adding avocado oil to our selection of products. The oil will be packaged in round Velmora bottles and we are looking for a simple and elegant label design highlighting both culinary and health benefits of avocado oil. The label size should be a one piece square, approx. 5.5 x 5.5 inches (14 x 14 cm). The oil will be sold under brand name Verdelune. Most label designs currently on the market feature some form of the avocado fruit, some have a depiction of oil extracted from the fruit, etc. but we are obviously open to other ideas and don't want to constrain designer's creativity in any way. The label should be designed to wrap around the bottle in one piece. Attached images are for inspiration only

Target Market(s)

Upscale, health conscious consumers

Requirements
Must have
• In addition to graphics:

- Brand name (Verdelune)
- Extra Virgin
- Avocado Oil
- First Cold pressed
- 8.45 oz / 250 ml
- space for bar code with EAN number (will be provided), and approx 0.75" x 1.5" blank space for Batch Number and Best Before date to be printed during bottling
- space for nutritional label (will be provided)
- Ingredients : 100% Pure Extra Virgin Avocado Oil
- "High in vitamin E, heart healthy monounsaturated fats, antioxidants, lutein and beta sitosterol"
- "Non GMO, does not contain trans fats, cholesterol, preservatives or artificial ingredients"
- "High smoke point (500F/260C), perfect for high heat cooking, salads, marinades and baking"
- "Store in a cool dark place"

```html
<!DOCTYPE html>
<html lang="en">
<head>
<meta charset="utf-8">
<title>Verdelune Avocado Oil Label</title>
<link rel="stylesheet" href="https://fonts.googleapis.com/css2?family=Source+Sans+3:wght@300;400;600;700&family=Archivo:wght@400;700;800&display=swap">
<style>
  :root {
    --leaf: #94ac12;
    --forest: #2f4f0a;
    --gold: #a27c10;
    --gold-soft: #efe6b8;
    --ink: #1f3a08;
    --frame: #8c8c8c;
    --paper: #ffffff;
    --wash-1: #cfe8b4;
    --wash-2: #8fbf78;
  }
  * { box-sizing: border-box; margin: 0; padding: 0; }
  html, body { width: 1200px; height: 1200px; overflow: hidden; background: var(--paper); }
  body { position: relative; font-family: "Source Sans 3", sans-serif; color: var(--ink); }

  .label { position: absolute; left: 194px; top: 194px; width: 820px; height: 820px; border: 1px solid var(--frame); }
  .abs { position: absolute; }

  /* Nutrition panel */
  .nutrition-frame { left: 20px; top: 28px; width: 198px; height: 311px; border: 2px solid var(--gold-soft); }
  .nutrition { left: 35px; top: 43px; width: 166px; height: 282px; border: 1px solid var(--gold); padding: 4px 7px; font-family: "Archivo", sans-serif; color: var(--gold); font-size: 6.6px; line-height: 1.2; }
  .nutrition h2 { font-size: 17px; font-weight: 800; line-height: 1.1; white-space: nowrap; }
  .nf-row { display: flex; justify-content: space-between; border-bottom: 0.6px solid var(--gold); padding: 2.5px 0 2px; }
  .nf-row.plain { border-bottom: none; padding: 0; }
  .nf-row.indent { padding-left: 12px; }
  .nf-bar { height: 5px; background: var(--gold); margin: 2px 0; }
  .nf-rule { height: 2.5px; background: var(--gold); margin: 1px 0; }
  .nf-b { font-weight: 700; }
  .nf-right { text-align: right; font-size: 4.6px; font-weight: 700; padding: 2px 0; border-bottom: 0.6px solid var(--gold); }
  .nf-note { font-size: 4.6px; padding: 3px 0 2px; }

  /* Copy column */
  .copy { left: 15px; width: 240px; font-size: 14px; line-height: 17.5px; }
  .copy strong { font-weight: 700; }
  .storage { left: 34px; top: 782px; font-size: 10.5px; line-height: 13.5px; font-weight: 700; }

  /* Front panel */
  .brand { left: 256px; top: 40px; width: 310px; text-align: center; font-weight: 700; font-size: 64px; line-height: 1; color: var(--leaf); }
  .organic { left: 256px; top: 118px; width: 310px; text-align: center; font-size: 41px; font-weight: 400; color: var(--forest); line-height: 1; }
  .fruit-art { left: 266px; top: 182px; width: 300px; height: 302px; }
  .product { left: 256px; top: 490px; width: 310px; text-align: center; font-weight: 700; font-size: 46px; line-height: 1; color: var(--leaf); }
  .grade { left: 256px; top: 552px; width: 310px; text-align: center; font-size: 31px; font-weight: 600; color: var(--gold); line-height: 1; }
  .process { left: 298px; top: 650px; font-size: 44px; font-weight: 300; line-height: 52px; color: var(--gold); }
  .net { left: 305px; top: 785px; font-size: 19px; color: var(--gold); }

  /* Side panel */
  .splash { left: 575px; top: 194px; width: 231px; height: 193px; }
  .brand-vertical { left: 580px; top: 62px; width: 220px; height: 510px; writing-mode: vertical-rl; text-align: center; font-weight: 700; font-size: 104px; line-height: 220px; color: var(--leaf); }
  .barcode-space { left: 580px; top: 648px; width: 224px; height: 122px; background: var(--leaf); color: var(--paper); font-weight: 700; font-size: 15px; line-height: 18px; padding: 42px 0 0 33px; }
</style>
</head>
<body>
<main class="label">

  <section class="abs nutrition-frame" aria-label="Nutrition facts panel"></section>
  <div class="abs nutrition">
    <h2>Nutrition Facts</h2>
    <div class="nf-row plain"><span>Serving Size</span><span>...g</span></div>
    <div class="nf-row plain"><span>Servings Per Container</span></div>
    <div class="nf-bar"></div>
    <div class="nf-row plain nf-b"><span>Amount Per Serving</span></div>
    <div class="nf-rule" style="height:0.6px"></div>
    <div class="nf-row plain"><span><span class="nf-b">Calories</span> ....</span><span>Calories from Fat ...</span></div>
    <div class="nf-rule"></div>
    <div class="nf-right">% Daily Value*</div>
    <div class="nf-row"><span><span class="nf-b">Total Fat</span> ...g</span><span class="nf-b">...%</span></div>
    <div class="nf-row indent"><span>Saturated Fat ...g</span><span class="nf-b">...%</span></div>
    <div class="nf-row indent"><span><em>Trans</em> Fat ...g</span></div>
    <div class="nf-row"><span><span class="nf-b">Cholestrol</span> ...mg</span><span class="nf-b">...%</span></div>
    <div class="nf-row"><span><span class="nf-b">Sodium</span> ...mg</span><span class="nf-b">...%</span></div>
    <div class="nf-row"><span><span class="nf-b">Total Carbohydrate</span> ...g</span><span class="nf-b">...%</span></div>
    <div class="nf-row indent"><span>Dietary Fiber ...g</span><span class="nf-b">...%</span></div>
    <div class="nf-row indent"><span>Sugars ...g</span></div>
    <div class="nf-row plain"><span><span class="nf-b">Protein</span> ...g</span></div>
    <div class="nf-bar"></div>
    <div class="nf-row"><span>Vitamin A</span><span class="nf-b">...%</span></div>
    <div class="nf-row"><span>Vitamin C</span><span class="nf-b">...%</span></div>
    <div class="nf-row"><span>Calcium</span><span class="nf-b">...%</span></div>
    <div class="nf-row"><span>Iron</span><span class="nf-b">...%</span></div>
    <p class="nf-note">*Percent Daily Values are based on a 2,000 calorie diet. Your Daily Values may be higer or lower depending on your calorie needs.</p>
    <div class="nf-rule" style="height:1.5px"></div>
  </div>

  <p class="abs copy" style="top:392px"><strong>Ingredients:</strong><br>100% Pure Extra Virgin Avocado Oil</p>
  <p class="abs copy" style="top:487px">High in vitamin E,<br>heart healthy monounsaturated fats,<br>antioxidants, lutein and beta sitosterol</p>
  <p class="abs copy" style="top:587px">Non GMO, does not contain trans fats,<br>cholesterol, preservatives or artificial<br>ingredients"</p>
  <p class="abs copy" style="top:682px">High smoke point <strong>(500F/260C)</strong>,<br>perfect for high heat cooking,<br>salads, marinades, and baking"</p>
  <p class="abs storage">Store in a<br>cool dark place</p>

  <h1 class="abs brand">Verdelune</h1>
  <p class="abs organic">Organic</p>
  <svg class="abs fruit-art" role="img" aria-label="Watercolour illustration of avocado halves with a leaf on a green splash" viewBox="0 0 300 302">
    <defs>
      <radialGradient id="fruitWash" cx="50%" cy="55%" r="55%">
        <stop offset="0" stop-color="var(--wash-2)"/>
        <stop offset="0.6" stop-color="var(--wash-1)"/>
        <stop offset="1" stop-color="#ffffff" stop-opacity="0"/>
      </radialGradient>
    </defs>
    <rect width="300" height="302" fill="url(#fruitWash)"/>
  </svg>
  <h2 class="abs product">Avocado Oil</h2>
  <p class="abs grade">Extra Virgin</p>
  <p class="abs process">First Cold<br>Pressed</p>
  <p class="abs net">NET WT 8.45 oz ( 250 ml)</p>

  <svg class="abs splash" role="img" aria-label="Soft green watercolour splash behind the brand name" viewBox="0 0 231 193">
    <defs>
      <radialGradient id="sideWash" cx="50%" cy="50%" r="55%">
        <stop offset="0" stop-color="var(--wash-1)"/>
        <stop offset="1" stop-color="#ffffff" stop-opacity="0"/>
      </radialGradient>
    </defs>
    <rect width="231" height="193" fill="url(#sideWash)"/>
  </svg>
  <p class="abs brand-vertical">Verdelune</p>

  <div class="abs barcode-space">space for bar code with<br>EAN number</div>

</main>
</body>
</html>
```